Business Card Design

We need a new business card design for our corporate executives. We are a very niche business working in the Aviation Night Vision Goggle Industry. I am looking for a design that has a "corporate" look and feel. I would like to see designs that incorporate a clean look with possibly raised letters, foil, or any other current design elements available. I am open to design elements/information being placed on the back of the business card but also want to be able to write on the back of the card to take notes. Back-side design is not mandatory.

Company Overview
At Harbor Lumen Systems, the most experienced team implements the highest quality night vision equipment, maintenance, and training procedures available to offer a comprehensive Night Vision Solution that enhances the safety and operational capabilities of all aviation organizations.

Our team is dedicated to client success and satisfaction throughout the entire night vision goggle solution lifecycle. Our solutions are designed to meet customer operational needs so that organizations can efficiently and effectively realize their goals – while increasing performance, reducing costs and enhancing safety.

Industry/Entity Type

Training

Contact Information for Business Card

Gregory T. Pellham, President, Harbor Lumen Systems, Inc., harborlumensystems.example, gregory.pellham@harborlumensystems.example, (555) 204-7716, (company toll free #) (855) 410-2957

```html
<!DOCTYPE html>
<html lang="en">
<head>
<meta charset="utf-8">
<title>Harbor Lumen Systems — Business Card</title>
<link href="https://fonts.googleapis.com/css2?family=Source+Sans+3:wght@400;600;700&display=swap" rel="stylesheet">
<style>
  :root {
    --backdrop: #7a5f43;
    --card-white: #f4f5f3;
    --card-white-edge: #e3e5e2;
    --lime: #9ccd1c;
    --lime-deep: #7fb010;
    --ink: #17191a;
    --ink-soft: #2a2d2f;
    --text-dark: #1f2326;
    --text-light: #d9dcdc;
    --text-muted: #9aa0a2;
    --rule: #55595b;
  }
  * { box-sizing: border-box; margin: 0; padding: 0; }
  html, body {
    width: 1200px; height: 1023px; overflow: hidden;
    background: var(--backdrop);
    font-family: "Source Sans 3", "Helvetica Neue", Arial, sans-serif;
  }
  .canvas { position: relative; width: 1200px; height: 1023px; }

  .card {
    position: absolute;
    width: 600px; height: 343px;
    border-radius: 4px;
    overflow: hidden;
    box-shadow: 0 14px 30px rgba(0,0,0,.45);
  }

  /* Front */
  .card-front { left: 70px; top: 100px; background: var(--ink); }
  .front-brand {
    height: 150px;
    background: linear-gradient(180deg, #ffffff, var(--card-white) 60%, var(--card-white-edge));
    display: flex; align-items: center; padding-left: 48px; gap: 16px;
  }
  .brand-dot {
    width: 30px; height: 30px; border-radius: 50%;
    background: var(--lime-deep);
    flex: none;
  }
  .brand-name {
    font-weight: 700; font-size: 38px; letter-spacing: .5px;
    color: var(--text-dark); text-transform: uppercase;
  }
  .front-band {
    height: 44px;
    background: linear-gradient(180deg, var(--lime), var(--lime-deep));
    display: flex; align-items: center; padding-left: 48px; gap: 10px;
    color: var(--text-dark);
  }
  .person-name { font-weight: 700; font-size: 24px; }
  .divider { width: 1.5px; height: 24px; background: var(--text-dark); }
  .person-title { font-size: 17px; font-weight: 400; }
  .front-contact {
    height: 149px;
    background: linear-gradient(160deg, var(--ink-soft), var(--ink) 70%);
    display: flex; justify-content: space-between;
    padding: 28px 40px 0 48px;
    color: var(--text-light);
  }
  .contact-list { list-style: none; font-size: 15px; line-height: 25px; }
  .contact-list li { display: flex; align-items: center; gap: 10px; }
  .contact-icon { width: 14px; height: 14px; flex: none; }
  .contact-note { color: var(--text-muted); }
  .address { display: flex; gap: 12px; align-items: flex-start; font-size: 15px; line-height: 21px; }
  .pin-badge { width: 34px; height: 34px; flex: none; }

  /* Back */
  .card-back {
    left: 530px; top: 580px;
    background: radial-gradient(ellipse at 35% 30%, #3a3d3f, var(--ink) 65%);
  }
  .back-brand {
    position: absolute; left: 0; right: 0; top: 110px;
    display: flex; justify-content: center; align-items: center; gap: 16px;
  }
  .back-brand .brand-name { color: #eceeee; font-size: 36px; }
  .back-rule {
    position: absolute; left: 0; right: 0; top: 268px;
    height: 1px; background: var(--rule);
  }
  .back-web {
    position: absolute; left: 34px; top: 284px;
    display: flex; align-items: center; gap: 8px;
    color: var(--text-muted); font-size: 16px; letter-spacing: 1px;
  }
</style>
</head>
<body>
<div class="canvas">

  <section class="card card-front" aria-label="Business card front">
    <div class="front-brand">
      <span class="brand-dot"></span>
      <span class="brand-name">Harbor Lumen Systems</span>
    </div>
    <div class="front-band">
      <span class="person-name">Gregory T. Pellham</span>
      <span class="divider"></span>
      <span class="person-title">President</span>
    </div>
    <div class="front-contact">
      <ul class="contact-list">
        <li>
          <svg class="contact-icon" viewBox="0 0 14 14"><circle cx="7" cy="7" r="6.3" fill="none" stroke="#9ccd1c" stroke-width="1.2"/><path d="M5 4l1 2-1 1 2 2 1-1 2 1-1 1.5c-2 0-4.5-2.5-4.5-4.5z" fill="#9ccd1c"/></svg>
          (555) 204-7716
        </li>
        <li>
          <svg class="contact-icon" viewBox="0 0 14 14"><circle cx="7" cy="7" r="6.3" fill="none" stroke="#9ccd1c" stroke-width="1.2"/><path d="M5 4l1 2-1 1 2 2 1-1 2 1-1 1.5c-2 0-4.5-2.5-4.5-4.5z" fill="#9ccd1c"/></svg>
          <span>(855) 410-2957 <span class="contact-note">[free]</span></span>
        </li>
        <li>
          <svg class="contact-icon" viewBox="0 0 14 14"><circle cx="7" cy="7" r="6.3" fill="none" stroke="#9ccd1c" stroke-width="1.2"/><rect x="3.8" y="4.8" width="6.4" height="4.4" fill="none" stroke="#9ccd1c"/><path d="M3.8 4.8l3.2 2.6 3.2-2.6" fill="none" stroke="#9ccd1c"/></svg>
          gregory.pellham@harborlumensystems.example
        </li>
      </ul>
      <div class="address">
        <svg class="pin-badge" viewBox="0 0 34 34"><circle cx="17" cy="17" r="15.5" fill="none" stroke="#9ccd1c" stroke-width="2"/><path d="M17 8a6 6 0 0 1 6 6c0 4.5-6 11-6 11s-6-6.5-6-11a6 6 0 0 1 6-6z" fill="#9ccd1c"/><circle cx="17" cy="14" r="2.2" fill="#17191a"/></svg>
        <p>2400 Alder Run<br>Suite 310 Linden,<br>Texas 75001</p>
      </div>
    </div>
  </section>

  <section class="card card-back" aria-label="Business card back">
    <div class="back-brand">
      <span class="brand-dot"></span>
      <span class="brand-name">Harbor Lumen Systems</span>
    </div>
    <div class="back-rule"></div>
    <div class="back-web">
      <svg class="contact-icon" viewBox="0 0 14 14"><circle cx="7" cy="7" r="6" fill="none" stroke="#9aa0a2" stroke-width="1.2"/><ellipse cx="7" cy="7" rx="2.5" ry="6" fill="none" stroke="#9aa0a2"/><path d="M1 7h12" stroke="#9aa0a2"/></svg>
      harborlumensystems.example
    </div>
  </section>

</div>
</body>
</html>
```